Looking for awesome business card design with attached existing logo

We are a water, mold, and fire damage restoration company called "Torvane Seco" Looking for an awesome business card that is edgy yet professional and unique. Show me what you got!

```html
<!DOCTYPE html>
<html lang="en">
<head>
<meta charset="UTF-8">
<title>Torvane Seco – Business Card</title>
<link href="https://fonts.googleapis.com/css2?family=Montserrat:wght@400;500;700&display=swap" rel="stylesheet">
<style>
  :root {
    --stage: #2b2624;
    --paper: #ffffff;
    --ink-dark: #1b1b1b;
    --brand-red: #e31b23;
    --brand-navy: #2d4a57;
    --brand-gold: #d4962a;
    --text-light: #f2f2f2;
  }
  * { box-sizing: border-box; margin: 0; padding: 0; }
  html, body {
    width: 1200px; height: 786px; overflow: hidden;
    background: var(--stage);
    font-family: "Montserrat", sans-serif;
  }
  .stage {
    position: relative; width: 1200px; height: 786px;
    display: flex; align-items: center; justify-content: center; gap: 50px;
  }
  .card {
    position: relative; width: 520px; height: 298px;
    background: var(--paper); overflow: hidden;
    box-shadow: 0 10px 30px rgba(0,0,0,.45);
  }
  .card-front { border-bottom: 5px solid var(--brand-red); }
  .wave { position: absolute; inset: 0; width: 100%; height: 100%; }
  .wordmark {
    position: absolute; display: flex; align-items: center; gap: 10px;
    font-weight: 700; color: var(--brand-navy);
    letter-spacing: .04em; text-transform: uppercase; white-space: nowrap;
  }
  .wordmark-dot { border-radius: 50%; background: var(--brand-gold); }
  .card-back .wordmark { top: 58px; right: 40px; font-size: 26px; }
  .card-back .wordmark-dot { width: 14px; height: 14px; }
  .card-front .wordmark {
    top: 50%; left: 50%; transform: translate(-50%, -50%); font-size: 38px;
  }
  .card-front .wordmark-dot { width: 20px; height: 20px; }
  .contact {
    position: absolute; left: 34px; bottom: 22px; color: var(--text-light);
    font-size: 11.5px; line-height: 1.5;
  }
  .contact-name {
    color: var(--brand-red); font-weight: 700; font-size: 18px;
    text-transform: uppercase; letter-spacing: .02em; line-height: 1.1;
  }
  .contact-role { margin-bottom: 8px; }
  .contact-address { margin-bottom: 8px; }
  .contact-line { display: flex; align-items: center; gap: 8px; }
  .contact-icon { width: 11px; height: 11px; fill: var(--brand-red); flex: none; }
</style>
</head>
<body>
<main class="stage">
  <section class="card card-back">
    <svg class="wave" viewBox="0 0 520 298" preserveAspectRatio="none" aria-hidden="true">
      <path d="M0,128 C120,136 250,124 330,122 C410,120 450,160 478,298 L0,298 Z" fill="var(--ink-dark)"/>
      <path d="M20,118 C140,126 250,114 335,110 C420,106 470,150 500,298 L486,298 C458,170 418,126 336,128 C250,130 130,140 20,122 Z" fill="var(--brand-red)"/>
    </svg>
    <div class="wordmark"><span class="wordmark-dot"></span>Torvane Seco</div>
    <div class="contact">
      <p class="contact-name">Martin Hale</p>
      <p class="contact-role">Managing Director</p>
      <p class="contact-address">Your address, City<br>State, Zip 1234</p>
      <p class="contact-line">
        <svg class="contact-icon" viewBox="0 0 24 24"><path d="M6.6 10.8a15.1 15.1 0 0 0 6.6 6.6l2.2-2.2a1 1 0 0 1 1-.25 11.4 11.4 0 0 0 3.6.57 1 1 0 0 1 1 1V20a1 1 0 0 1-1 1A17 17 0 0 1 3 4a1 1 0 0 1 1-1h3.5a1 1 0 0 1 1 1c0 1.25.2 2.45.57 3.57a1 1 0 0 1-.25 1z"/></svg>
        123 456 789
      </p>
      <p class="contact-line">
        <svg class="contact-icon" viewBox="0 0 24 24"><path d="M2 5h20v14H2z M2 5l10 8 10-8" fill="var(--brand-red)"/><path d="M3 6l9 7 9-7" fill="none" stroke="var(--ink-dark)" stroke-width="1.6"/></svg>
        info@torvaneseco.com
      </p>
      <p class="contact-line">
        <svg class="contact-icon" viewBox="0 0 24 24"><circle cx="12" cy="12" r="10"/><path d="M2 12h20M12 2c3 3 3 17 0 20M12 2c-3 3-3 17 0 20" fill="none" stroke="var(--ink-dark)" stroke-width="1.4"/></svg>
        www.torvaneseco.com
      </p>
    </div>
  </section>

  <section class="card card-front">
    <div class="wordmark"><span class="wordmark-dot"></span>Torvane Seco</div>
  </section>
</main>
</body>
</html>
```